Gaming Related Website

GuildWeave.com is a forum for gamers to connect online.

We would like a design for our front page.

Please feel free to include a basic logo.

Please take a look at the following sites for inspiration:
http://uk.plaryx.com/
http://eu.fraygrid.net/en/
http://www.stormvantor.com/

Target Market(s)

On-line gamers on consoles and PCs

Industry/Entity Type

Online

Requirements
Must have
• Please follow the wireframes attached.

```html
<!DOCTYPE html>
<html lang="en">
<head>
<meta charset="utf-8">
<title>GuildWeave – Communities</title>
<link rel="stylesheet" href="https://fonts.googleapis.com/css2?family=Ubuntu:wght@400;500;700&display=swap">
<style>
:root{
  --page:#1b1b1b;
  --panel:#030303;
  --feed:#0d0d0d;
  --line:#2c2c2c;
  --text:#e6e6e6;
  --muted:#8a8a8a;
  --accent:#1ba6cc;
  --btn-border:#9a9a9a;
}
*{box-sizing:border-box;margin:0;padding:0}
html,body{width:1200px;height:960px;overflow:hidden;background:var(--page)}
body{font-family:"Ubuntu",sans-serif;color:var(--text)}
.stage{position:absolute;left:0;top:0;width:1400px;height:1120px;transform:scale(.857142857);transform-origin:0 0;background:var(--page)}
.abs{position:absolute}

/* header */
.site-header{position:absolute;left:0;top:0;width:1400px;height:80px;background:linear-gradient(#2b2b2b,#0b0b0b);border-bottom:1px solid #3a3a3a}
.brand{position:absolute;left:220px;top:24px;font-size:27px;font-weight:700;letter-spacing:1px;color:#d9d9d9}
.main-nav{position:absolute;left:424px;top:0;height:80px;display:flex;border-left:1px solid #333}
.main-nav a{display:flex;align-items:center;justify-content:center;height:80px;padding:0 4px;border-right:1px solid #333;color:#e0e0e0;font-size:14px;text-decoration:none;line-height:20px;text-align:center;white-space:nowrap}
.main-nav a.active{background:linear-gradient(#161616 30%,#0e5d72);color:#fff}
.header-glow{position:absolute;left:220px;top:80px;width:160px;height:30px;background:radial-gradient(ellipse at 50% 0,rgba(255,255,255,.12),transparent 70%)}

/* panels */
.panel{position:absolute;background:var(--panel);border:1px solid #333}
.btn{display:inline-block;border:1px solid var(--btn-border);color:var(--muted);font-size:13px;text-align:center;line-height:22px;padding:0 9px;background:#0a0a0a;white-space:nowrap}
.btn.on{border-color:var(--accent);color:#fff;box-shadow:0 0 0 1px #0a4050}
.btn.big{font-size:15px;line-height:25px;color:#8f8f8f}
.btn.wide{width:160px;padding:0;font-size:13.5px}

/* profile */
.avatar{position:absolute;left:241px;top:142px;width:56px;height:56px;background:linear-gradient(135deg,#6b5040,#2a1e18 60%,#a08070)}
.user-name{position:absolute;left:306px;top:141px;color:var(--accent);font-size:17px;font-weight:500}
.user-links{position:absolute;left:306px;top:164px;font-size:11px;color:#cfcfcf;line-height:18px}
.stats{position:absolute;left:230px;top:228px;width:182px;height:60px;border:1px solid #aaa;display:flex;justify-content:space-between;padding:8px 5px 0}
.stats div{text-align:center;font-size:11px;line-height:14px}
.stats b{display:block;font-size:18px;font-weight:700;line-height:24px}

/* game list */
.game-list{position:absolute;left:221px;top:369px;width:200px;list-style:none}
.game-list li{height:37px;line-height:37px;text-align:center;font-size:15px;color:#e8e8e8;white-space:nowrap}
.game-list li.selected{margin:0 9px;border:1px solid var(--accent);line-height:35px}

/* tabs */
.tab{position:absolute;font-size:13px;line-height:22px;padding:0 9px;color:#fff;background:#000;border-top:1px solid #333;white-space:nowrap}
.tab.off{background:#1b1b1b;color:#6f6f6f;border-top:1px solid #2a2a2a}

/* feed */
.filter-label{position:absolute;left:448px;top:168px;font-size:14px}
.filters{position:absolute;left:449px;top:195px;display:flex;gap:11px;font-size:14px;white-space:nowrap}
.filters span{display:flex;align-items:center;gap:5px}
.filters i{display:inline-block;width:15px;height:15px;background:linear-gradient(#777,#3a3a3a)}
.feed{position:absolute;left:447px;top:233px;width:505px;height:710px;background:var(--feed)}
.feed-item{margin:0 17px;padding:13px 0 0 5px;border-bottom:1px solid var(--line);font-size:14px;line-height:23px}
.feed-item:last-of-type{border-bottom:none}
.feed-item .muted{color:#aaa}
.feed-actions{margin-top:11px;display:flex;gap:6px}

.side-row{position:absolute;font-size:14px;white-space:nowrap}
.footer{position:absolute;left:0;top:1003px;width:1400px;height:117px;background:linear-gradient(#1e1e1e,#0b0b0b);border-top:1px solid #333;text-align:center;font-size:13px;color:#b5b5b5;line-height:18px;padding-top:20px}
.footer p+p{margin-top:14px}
</style>
</head>
<body>
<div class="stage">
  <header class="site-header">
    <div class="brand">GUILDWEAVE</div>
    <nav class="main-nav">
      <a style="width:89px">HEADLINES</a>
      <a style="width:72px">FORUMS</a>
      <a class="active" style="width:108px">COMMUNITIES</a>
      <a style="width:100px">CHALLENGES</a>
      <a style="width:101px">GAMES INFO/<br>DOWNLOADS</a>
      <a style="width:114px">COMPETITIONS</a>
      <a style="width:115px">ACHIEVEMENTS</a>
      <a style="width:60px">TEAMS</a>
    </nav>
  </header>
  <div class="header-glow"></div>

  <!-- profile -->
  <section class="panel" style="left:220px;top:120px;width:202px;height:202px"></section>
  <div class="avatar" role="img" aria-label="Profile photo of the user"></div>
  <div class="user-name">John Doe</div>
  <div class="user-links">EDIT &nbsp;|&nbsp; LOG OUT<br>GAMING STATS</div>
  <div class="stats">
    <div><b>16</b>GAMES</div>
    <div><b>3</b>COMMUNITIES</div>
    <div><b>2</b>TEAMS</div>
  </div>

  <!-- games -->
  <section class="panel" style="left:220px;top:342px;width:202px;height:622px"></section>
  <ul class="game-list">
    <li>All Games</li><li>Deep Frontier</li><li>Rimlands 2</li>
    <li class="selected">Shadow Oath III</li>
    <li>Line Of Fire: Dark Ops 2</li><li>Clan Clash</li><li>Badge Of Valor</li>
    <li>Battlerunner</li><li>Realm Of Runecraft</li><li>Pitch Pro 2012</li>
    <li>Iron Stealth Core</li><li>Street Heist V</li><li>Infernum III</li><li>Top Speed: Outlaws</li>
  </ul>
  <span class="btn big abs" style="left:258px;top:897px;width:126px">LOAD MORE</span>

  <!-- newsfeed -->
  <div class="tab" style="left:835px;top:125px">Newsfeed</div>
  <div class="tab off" style="left:914px;top:125px">Chats</div>
  <section class="panel" style="left:431px;top:147px;width:537px;height:817px"></section>
  <div class="filter-label">Fliter By:</div>
  <div class="filters">
    <span><i></i>Notifications</span><span><i></i>My Communities</span><span><i></i>My Teams</span><span><i></i>My Competitions</span>
  </div>
  <div class="feed">
    <div class="feed-item" style="height:113px">You have been challenged by Pokri for a 1v1 game of Tremor Arena<br>at 12:40, Today
      <div class="feed-actions"><span class="btn on">ACCEPT</span><span class="btn">DECLINE</span></div></div>
    <div class="feed-item" style="height:50px">New Patch Is Out For Realm Of Runecraft &nbsp;<span class="muted">(Read More)</span></div>
    <div class="feed-item" style="height:76px">Lorem ipsum dolor sit amet, consectetur adipiscing elit. Donec quis convallis est.</div>
    <div class="feed-item" style="height:78px">Sed sodales pulvinar nisi, eget fringilla mi tempus id. Integer scelerisque augue in risus vehicula vulputate fringilla elit sodales.</div>
    <div class="feed-item" style="height:115px">You have been challenged by GXX76 for a 1v1 game of Tremor Arena<br>at 16:30, Today
      <div class="feed-actions"><span class="btn">ACCEPT</span><span class="btn">DECLINE</span></div></div>
    <div class="feed-item" style="height:50px">New Patch Is Out For Realm Of Runecraft &nbsp;<span class="muted">(Read More)</span></div>
    <div class="feed-item" style="height:76px">Lorem ipsum dolor sit amet, consectetur adipiscing elit. Donec quis convallis est.</div>
    <div class="feed-item" style="height:78px">Sed sodales pulvinar nisi, eget fringilla mi tempus id. Integer scelerisque augue in risus vehicula vulputate fringilla elit sodales.</div>
  </div>
  <span class="btn big abs" style="left:632px;top:882px;width:126px">LOAD MORE</span>

  <!-- servers -->
  <div class="tab" style="left:979px;top:124px">Game Servers</div>
  <div class="tab off" style="left:1077px;top:124px">VOIP Channels</div>
  <section class="panel" style="left:978px;top:146px;width:202px;height:201px"></section>
  <div class="side-row" style="left:986px;top:166px">Stormfield 3.....32/18</div>
  <span class="btn on abs" style="left:1131px;top:165px;padding:0 7px">JOIN</span>
  <span class="btn big wide abs" style="left:999px;top:299px">ADD A GAME SERVER</span>

  <!-- communities -->
  <div class="tab" style="left:979px;top:368px">My Communities</div>
  <div class="tab off" style="left:1092px;top:368px;padding:0 16px">My Teams</div>
  <section class="panel" style="left:978px;top:390px;width:202px;height:201px"></section>
  <div class="side-row" style="left:988px;top:411px">Game Quorom..........8 Online</div>
  <span class="btn big wide abs" style="left:999px;top:543px">SET UP A COMMUNITY</span>

  <footer class="footer">
    <p>List Of members, filtered by Game, Community, Team or any combination of the three. For just the games<br>the system wil show how many players are online</p>
    <p>Copyright 2012 GuildWeave.com. All Rights Reserved</p>
  </footer>
</div>
</body>
</html>
```